Design some stationary for Quiet Taverns

Quiet Taverns would like minimalist style business stationary, Notecards or Postcard (148mm x 105mm), Business Cards (84mm x 55mm), MiniCards (70mm x 28mm), specs at: [url removed, login to view] . We are open to any ideas you may have.

It is estimated that there are around 9 million deaf and hard of hearing people in the UK, all of whom through our website are potential customers.

The site provides information regarding social events to deaf people their families, friends and professionals alike.

The site provides information on deaf pub groups throughout the UK and offers information on transport and deaf friendly places to stay. These events take place at venues all over the UK and deaf people travel regularly to attend.
Quiet Taverns have official logo which is attached.

```html
<!DOCTYPE html>
<html lang="en">
<head>
<meta charset="utf-8">
<title>Quiet Taverns Stationery</title>
<link href="https://fonts.googleapis.com/css2?family=Open+Sans:wght@400;600;700&display=swap" rel="stylesheet">
<style>
  :root {
    --ink: #111111;
    --paper: #ffffff;
    --backdrop: #ffffff;
    --shadow: rgba(0, 0, 0, 0.28);
    --rule: #222222;
  }
  * { box-sizing: border-box; margin: 0; padding: 0; }
  html, body {
    width: 1200px; height: 909px; overflow: hidden;
    background: var(--backdrop);
    font-family: "Open Sans", Arial, sans-serif;
    color: var(--ink);
  }
  .canvas { position: relative; width: 1200px; height: 909px; }
  .sheet {
    position: absolute; background: var(--paper);
    box-shadow: 3px 4px 8px var(--shadow);
    overflow: hidden;
  }
  .sheet > * { position: absolute; }
  .bar { top: 0; bottom: 0; background: var(--ink); }
  .mark { border-radius: 50%; background: var(--ink); }
  .wordmark { font-weight: 600; letter-spacing: -0.02em; white-space: nowrap; line-height: 1; }
  .url { font-weight: 600; white-space: nowrap; line-height: 1; letter-spacing: 0.02em; }

  .contact-list { display: flex; flex-direction: column; }
  .contact { font-weight: 700; white-space: nowrap; line-height: 1; display: flex; align-items: center; }
  .icon { flex: none; display: flex; align-items: center; justify-content: center; }
  .social-box { display: block; border: 1.5px solid var(--ink); border-radius: 2px; }
  .divider { width: 2px; background: var(--rule); }

  /* letterhead */
  .letterhead { left: 60px; top: 24px; width: 604px; height: 857px; }
  .letterhead .bar { left: 40px; width: 13px; }
  .letterhead .mark { left: 24px; top: 56px; width: 80px; height: 80px; }
  .letterhead .wordmark { left: 113px; top: 16px; font-size: 30px; }
  .letterhead .url { left: 114px; top: 52px; font-size: 14px; }
  .letterhead .contact-list { top: 798px; gap: 8px; }
  .letterhead .contact { height: 16px; font-size: 13px; gap: 8px; }
  .letterhead .contact.phone { font-size: 15px; }
  .letterhead .icon { width: 20px; }
  .letterhead .social-box { width: 15px; height: 15px; }
  .letterhead .col-direct { left: 96px; }
  .letterhead .divider { left: 326px; top: 792px; height: 46px; }
  .letterhead .col-social { left: 356px; }

  /* business card */
  .card-large { left: 716px; top: 127px; width: 427px; height: 302px; }
  .card-large .bar { left: 44px; width: 17px; }
  .card-large .mark { left: 24px; top: 94px; width: 112px; height: 112px; }
  .card-large .wordmark { left: 171px; top: 34px; font-size: 34px; }
  .card-large .url { left: 172px; top: 80px; font-size: 18px; }
  .card-large .contact-list { left: 170px; top: 150px; gap: 8px; }
  .card-large .contact { height: 16px; font-size: 12px; gap: 8px; }
  .card-large .contact.phone { font-size: 14px; }
  .card-large .contact.gap-before { margin-top: 14px; }
  .card-large .icon { width: 18px; }
  .card-large .social-box { width: 16px; height: 16px; }

  /* medium card */
  .card-medium { left: 716px; top: 484px; width: 241px; height: 160px; }
  .card-medium .bar { left: 52px; width: 9px; }
  .card-medium .mark { left: 14px; top: 53px; width: 60px; height: 60px; }
  .card-medium .wordmark { left: 96px; top: 13px; font-size: 20px; }
  .card-medium .url { left: 97px; top: 40px; font-size: 10px; }
  .card-medium .contact-list { left: 96px; top: 74px; gap: 5px; }
  .card-medium .contact { height: 10px; font-size: 7px; gap: 5px; }
  .card-medium .contact.phone { font-size: 8.5px; }
  .card-medium .contact.gap-before { margin-top: 8px; }
  .card-medium .icon { width: 10px; }
  .card-medium .social-box { width: 9px; height: 9px; border-width: 1px; }

  /* mini card */
  .card-mini { left: 716px; top: 696px; width: 201px; height: 83px; }
  .card-mini .bar { left: 33px; width: 6px; }
  .card-mini .mark { left: 10px; top: 22px; width: 36px; height: 36px; }
  .card-mini .wordmark { left: 72px; top: 5px; font-size: 16px; }
  .card-mini .url { left: 73px; top: 25px; font-size: 8px; }
  .card-mini .contact-list { left: 73px; top: 37px; gap: 3px; }
  .card-mini .contact { height: 7px; font-size: 6px; gap: 4px; }
  .card-mini .icon { width: 7px; }
  .card-mini .social-box { width: 6px; height: 6px; border-width: 1px; }
</style>
</head>
<body>
<main class="canvas">

  <section class="sheet letterhead" aria-label="Letterhead">
    <div class="bar"></div>
    <div class="mark" role="img" aria-label="Quiet Taverns emblem"></div>
    <p class="wordmark">Quiet Taverns</p>
    <p class="url">www.quiettaverns.co.uk</p>
    <div class="contact-list col-direct">
      <p class="contact phone"><span class="icon"><svg width="12" height="17" viewBox="0 0 12 17"><rect x="1" y="1" width="10" height="15" rx="2" fill="none" stroke="#111" stroke-width="1.6"/><rect x="3" y="3.5" width="6" height="6" fill="#111"/></svg></span>07 000 318 642</p>
      <p class="contact"><span class="icon"><svg width="17" height="12" viewBox="0 0 17 12"><rect width="17" height="12" fill="#111"/><path d="M0 0 L8.5 7 L17 0" fill="none" stroke="#fff" stroke-width="1.3"/></svg></span>hello@quiettaverns.co.uk</p>
    </div>
    <div class="divider"></div>
    <div class="contact-list col-social">
      <p class="contact"><span class="icon"><span class="social-box"></span></span>quiettaverns.co.uk/meet</p>
      <p class="contact"><span class="icon"><span class="social-box"></span></span>@quiettaverns</p>
    </div>
  </section>

  <section class="sheet card-large" aria-label="Business card">
    <div class="bar"></div>
    <div class="mark" role="img" aria-label="Quiet Taverns emblem"></div>
    <p class="wordmark">Quiet Taverns</p>
    <p class="url">www.quiettaverns.co.uk</p>
    <div class="contact-list">
      <p class="contact phone"><span class="icon"><svg width="12" height="17" viewBox="0 0 12 17"><rect x="1" y="1" width="10" height="15" rx="2" fill="none" stroke="#111" stroke-width="1.6"/><rect x="3" y="3.5" width="6" height="6" fill="#111"/></svg></span>07 000 318 642</p>
      <p class="contact"><span class="icon"><svg width="16" height="11" viewBox="0 0 17 12"><rect width="17" height="12" fill="#111"/><path d="M0 0 L8.5 7 L17 0" fill="none" stroke="#fff" stroke-width="1.3"/></svg></span>hello@quiettaverns.co.uk</p>
      <p class="contact gap-before"><span class="icon"><span class="social-box"></span></span>quiettaverns.co.uk/meet</p>
      <p class="contact"><span class="icon"><span class="social-box"></span></span>@quiettaverns</p>
    </div>
  </section>

  <section class="sheet card-medium" aria-label="Medium card">
    <div class="bar"></div>
    <div class="mark" role="img" aria-label="Quiet Taverns emblem"></div>
    <p class="wordmark">Quiet Taverns</p>
    <p class="url">www.quiettaverns.co.uk</p>
    <div class="contact-list">
      <p class="contact phone"><span class="icon"><svg width="7" height="10" viewBox="0 0 12 17"><rect x="1" y="1" width="10" height="15" rx="2" fill="none" stroke="#111" stroke-width="2"/><rect x="3" y="3.5" width="6" height="6" fill="#111"/></svg></span>07 000 318 642</p>
      <p class="contact"><span class="icon"><svg width="9" height="6" viewBox="0 0 17 12"><rect width="17" height="12" fill="#111"/><path d="M0 0 L8.5 7 L17 0" fill="none" stroke="#fff" stroke-width="1.6"/></svg></span>hello@quiettaverns.co.uk</p>
      <p class="contact gap-before"><span class="icon"><span class="social-box"></span></span>quiettaverns.co.uk/meet</p>
      <p class="contact"><span class="icon"><span class="social-box"></span></span>@quiettaverns</p>
    </div>
  </section>

  <section class="sheet card-mini" aria-label="Mini card">
    <div class="bar"></div>
    <div class="mark" role="img" aria-label="Quiet Taverns emblem"></div>
    <p class="wordmark">Quiet Taverns</p>
    <p class="url">www.quiettaverns.co.uk</p>
    <div class="contact-list">
      <p class="contact"><span class="icon"><svg width="5" height="7" viewBox="0 0 12 17"><rect x="1" y="1" width="10" height="15" rx="2" fill="none" stroke="#111" stroke-width="2.4"/></svg></span>07 000 318 642</p>
      <p class="contact"><span class="icon"><svg width="6" height="4" viewBox="0 0 17 12"><rect width="17" height="12" fill="#111"/></svg></span>hello@quiettaverns.co.uk</p>
      <p class="contact"><span class="icon"><span class="social-box"></span></span>quiettaverns.co.uk/meet</p>
      <p class="contact"><span class="icon"><span class="social-box"></span></span>@quiettaverns</p>
    </div>
  </section>

</main>
</body>
</html>
```